Quillfern Nightclub Flyer (Updated)

Flyer for facebook, square is fine, or rectangular. Here is the text:
QUILLFERN
Nightclub + Lounge
presents

SPLIT DECK WEDNESDAY
Nov 29 2018

CLUB FLOOR:
GORDY B2B RALPH
THEODORE BRUSKVIK

LOUNGE:
OTIS B2B HALF TIDE
COPPER FENWICK

Powered by HALVERN Acoustics
4716 Larchmere Avenue 21+ 9pm-2am
quillfernvenue-example.com for VIP booth inquiries

Target Market(s)

Nightclub

Industry/Entity Type

Night Club

Font styles to use
Sans Serif

Colors

Designer to choose colors to be used in the design.

Requirements
Must have
• All the text listed, and plz keep the theme of the attached files. We want to stay consistent with the Quillfern brand
Nice to have
• Try to stay with the theme from the attachments
Should not have
• Dont' stray to far from the general theme we have from the attachments

```html
<!DOCTYPE html>
<html lang="en">
<head>
<meta charset="utf-8">
<title>Quillfern Nightclub – Split Deck Wednesday</title>
<link rel="stylesheet" href="https://fonts.googleapis.com/css2?family=Jost:wght@400;500&display=swap">
<style>
  :root {
    --paper-light: #f7eedb;
    --paper-mid: #ecdcb8;
    --paper-edge: #d9c497;
    --brand-brown: #6b4a2b;
    --ink-dark: #3a2a1c;
    --brocade-deep: #3d1a12;
    --brocade-mid: #5a2a1c;
    --text-cream: #f6eedc;
  }
  html, body {
    margin: 0;
    padding: 0;
    overflow: hidden;
    background: var(--paper-light);
  }
  .flyer {
    position: relative;
    width: 1200px;
    height: 690px;
    overflow: hidden;
    font-family: "Jost", "Century Gothic", sans-serif;
    background: radial-gradient(ellipse at 60% 50%, var(--paper-light) 0%, var(--paper-mid) 75%, var(--paper-edge) 100%);
  }
  .flyer-art {
    position: absolute;
    inset: 0;
    width: 1200px;
    height: 690px;
  }
  .brand {
    position: absolute;
    left: 30px;
    top: 200px;
    width: 340px;
    text-align: center;
    color: var(--brand-brown);
  }
  .brand-mark {
    width: 96px;
    height: 96px;
    margin: 0 auto 18px;
    border-radius: 50%;
    background: var(--brand-brown);
  }
  .brand-name {
    margin: 0;
    font-size: 46px;
    font-weight: 400;
    letter-spacing: 4px;
    line-height: 1;
  }
  .brand-tagline {
    margin: 10px 0 0;
    font-size: 18px;
    letter-spacing: 3px;
    line-height: 1;
  }
  .brand-presents {
    margin: 40px 0 0;
    font-size: 26px;
    line-height: 1;
  }
  .lineup {
    position: absolute;
    left: 454px;
    top: 178px;
    width: 500px;
    text-align: center;
    color: var(--text-cream);
    font-size: 22px;
    line-height: 36px;
    letter-spacing: 0.5px;
  }
  .lineup p { margin: 0; }
  .lineup .divider {
    display: block;
    width: 46px;
    height: 1px;
    margin: 12px auto 13px;
    background: var(--text-cream);
    opacity: 0.8;
  }
  .event-info {
    position: absolute;
    right: 30px;
    top: 546px;
    width: 330px;
    text-align: center;
    color: var(--ink-dark);
  }
  .event-info p { margin: 0; }
  .event-info .sponsor,
  .event-info .venue {
    font-size: 14px;
    line-height: 19px;
  }
  .event-info .web,
  .event-info .vip {
    font-size: 22px;
    line-height: 30px;
  }
</style>
</head>
<body>
<main class="flyer">
  <svg class="flyer-art" viewBox="0 0 1200 690" xmlns="http://www.w3.org/2000/svg">
    <defs>
      <linearGradient id="brocadeFill" x1="0" y1="0" x2="1" y2="1">
        <stop offset="0" stop-color="var(--brocade-mid)"/>
        <stop offset="0.5" stop-color="var(--brocade-deep)"/>
        <stop offset="1" stop-color="var(--brocade-mid)"/>
      </linearGradient>
    </defs>
    <path class="torn-shadow" d="M704 14 L1008 348 L704 684 L400 348 Z" fill="#cbb283" opacity="0.55"/>
    <path class="torn-lip" d="M704 22 L998 348 L704 674 L410 348 Z" fill="#f8f0de"/>
    <path class="brocade-window" role="img" aria-label="Dark maroon damask brocade pattern revealed through torn paper"
          d="M704 40 C760 110 900 260 978 348 C900 436 760 590 704 656 C648 590 508 436 430 348 C508 260 648 110 704 40 Z"
          fill="url(#brocadeFill)"/>
  </svg>

  <section class="brand">
    <div class="brand-mark"></div>
    <h1 class="brand-name">QUILLFERN</h1>
    <p class="brand-tagline">NIGHTCLUB + LOUNGE</p>
    <p class="brand-presents">presents</p>
  </section>

  <section class="lineup">
    <p class="event-title">SPLIT DECK WEDNESDAY</p>
    <p class="event-date">Nov 29 2018</p>
    <span class="divider"></span>
    <p class="room">CLUB FLOOR:</p>
    <p class="act">GORDY B2B RALPH</p>
    <p class="act">THEODORE BRUSKVIK</p>
    <span class="divider"></span>
    <p class="room">LOUNGE:</p>
    <p class="act">OTIS B2B HALF TIDE</p>
    <p class="act">COPPER FENWICK</p>
  </section>

  <section class="event-info">
    <p class="sponsor">Powered by HALVERN Acoustics</p>
    <p class="venue">4716 Larchmere Avenue 21+ 9pm-2am</p>
    <p class="web">quillfernvenue-example.com</p>
    <p class="vip">for VIP booth inquiries</p>
  </section>
</main>
</body>
</html>
```